Open Horizon Table - invitation / brochure

​​I am in need of a bi-fold invitation/brochure for an educational series called "Open Horizon Table". This dinner series provides education and community for "Women in Transition" these are women who are currently getting divorced, recently divorced, or widowed.

I am a partner of a wealth management boutique that advises a small number of high-net-worth families. Additionally, I am married to one of the most prominent family law attorneys in the country. The combination of these two unique perspectives has allowed me to see there is an unfortunate dearth of impactful, powerful, and useful resources to help wealthy women transition from being married to being single. (via divorce and/or death of their spouse)

What, How & WHY I do my job:
As a wealth manager, the "what" and "how" aspects of my job are not materially different from most of my competitors. However, the thing that makes me completely unique, and without competition, is "why" I do my job.

I do this because so many women experience unwelcome and unproductive feelings when the dilution of their marriage is complete AND because there is virtually no good place for them to obtain the important information they truly need to move forward and lead a happy, full, prosperous, productive, and fun life. In the absence of this information, many women experience unwelcome, unpleasant, and unproductive emotions.

For example, some experience shame or fear that they have failed. Others struggle with the belief they wasted a significant portion of their life. Some struggle with unresolved anger over the entire experience. It's very difficult to process and work through these emotions by yourself and it can be hard to get the support and guidance they need from their best friends (most are not trained in this area) may well be married (functional or otherwise) and they often times don't have the times to be there when the newly divorced or widowed women need them most.

Usually, these negative feelings are most intense when they are looking backward in time. However, I have seen women go on and lead remarkably impressive lives. Lives that are ​more ​full, richer, more fun, dynamic, and rewarding than they expected possible.

More about the WHY I do what I do - I created Open Horizon Table so women in transition have a safe, supportive and comfortable space for these women to support each other. While each woman's story is unique, the emotional consequences are fairly common and they do not need to feel alone as they process the sometimes difficult, conflicting, and unpredictable emotions.

I want them to connect with each other because they have a great appreciation and empathy for what all the other women are experiencing. A bi-product of attending and participating in the dinner is to forge friendships and connections with the other woman in attendance so they can be resources to each other when they need help dealing with their own fear, anxiety, or anger. IMPORTANT NOTE - THIS IS NOT A THERAPY OR SUPPORT GROUP. Instead, this is a select group of very successful and accomplished women who have a shared experience and while each is navigating their own path, they have an opportunity to learn important information, in a safe place, where they can share their experience, strength, and hope with each other.

I want the invitation/brochure to feel very bespoke, thoughtfully curated, and specifically designed to address the most important and impactful areas of life, health, and wellness. I want the invitation/brochure to communicate that the presenters are the best in class and thought leaders in their respective areas of expertise. I also want to communicate that they have so much to be excited about. Because they have substantial financial resources, they have a unique opportunity to reinvent themselves and lead a life beyond their wildest dreams. I hope they can see how and why they can stop feeling the negative feelings of anger, sadness, fear, guilt, remorse, and regret. My goal is to get them to look forward (as opposed to backward where the negative emotions come from) so they can be optimistic, excited, happy, joyful, and enthusiastic because they get to be whoever they want; live wherever and however they want. They are not defined nor controlled by their past. They have full control and abundant resources at their disposal to be happier and more fulfilled than they ever hoped or imagined.

The feelings of optimism, excitement, energetic, and joyfulness are very important to the messaging of the Open Horizon Table. I'd like this to be a consistent theme throughout the invitation/brochure. Basically moving from a dark, sad, and negative past to a bright, fun, optimistic, rewarding, fulfilling, and dynamic future.

To create an exciting, rewarding and vibrant life they will want to (in some cases need to) learn new information and skills from the leading authorities in the most important and impactful areas of life.

The presenters at each dinner will focus on one of the "8 Dimensions of Wellness" so they can make thoughtful and informed decisions without fear, anxiety, and stress.

If you think of marriage as two people sailing a ship or flying a plane, the husband and wife often divide the responsibilities of running their affairs because it's too much for one person to manage all by themselves; besides they have a spouse who can help and often times they have different expertise. For illustration purposes, let's say the husband manages the even-numbered items and the wife manages the odd number of items. Each manages half but together everything is well managed and nothing falls through the cracks.

Post-divorce, the husband and wife now each have their own boat to sail and are responsible for all the items (odd and even-numbered) of their ship.

Unfortunately, these women are having to manage items that she has little to no experience with the even-numbered items the husband used to manage during the marriage. They have to take sole control of complicated matters that have serious and long-lasting consequences. That's great if they do a good job. However, given the scope, scale, and complexity of 7-10 figure net worth chances are they won't have the experience, expertise, intellectual resources, and time to manage all the even and odd numbers optimally.

The format of the Open Horizon Table events will be an intimate dinner conversation, in a private room, at a 5 star restaurant in Chicago. There will be a thoughtfully curated group of 4-10 women at one round table to facilitate an interesting and informative presentation. It will be specifically curated for them and delivered. There is no cost to attend the event and they are welcome to attend as many as they like. I will be covering all the expenses related to dinner, drinks, valet parking, and the speaker or presenter.

Each monthly dinner will focus on 1 of the 8 Dimensions of Wellness:

1. Physical - Physical Activity, Good Nutrition, Sleep, Preventing Illness & Injury, and Managing Chronic Health Conditions.

2. Emotional - Coping Effectively with life and creating satisfying relationships.

3. Social - Developing a sense of connection, belonging, and a well-developed support system.

4. Intellectual - Recognizing one’s creative abilities and finding ways to expand knowledge and skills. Boost cognitive function, stimulate the brain, and fuel learning.

5. Environmental - Occupying pleasant, stimulating environments that support well-being.

6. Spiritual - Expanding a sense of purpose and meaning in life, including one’s morals and ethics. (May or may not involve religious activities). Meditation

7. Vocational - Gaining personal satisfaction and enrichment from one's work (maybe academic or professional). Share your talents, wisdom, and experience.

8. Financial - Satisfaction with current and future financial situations.

I'd like the invitation/brochure to give a general overview of the 8 dimensions of wellness and that each gathering will focus on one of the eight. The presentation will be done by women (some of whom went through a divorce or the death of a spouse) who are widely recognized as experts in their respective fields. The female presenters will be highly qualified and credentialed in their field - this could mean they are MDs or PhDs and/or have decades of experience in their specific area of expertise.

I'd like the invitation to be "timeless" meaning that it doesn't have specific dates, times, or locations included. However, if someone would like more information and details they can call or email me for the specific details of the next couple of dates, topics, locations, and menus. I am also open to having a QR code available on the brochure for them to contact me for additional information. Once they contact my office they will receive I will receive all the detailed information via a PDF so they can RSVP if they would like to attend. My goal is that I don't want the invitation/brochure to expire even though the event details change every month.

I will market the Open Horizon Table program by distributing the invitation/brochures available via therapists, divorce lawyers, and grief counselors that specialize in this demographic of women in transition. They in turn will share the invitation/brochure with their woman in transition clients if they think they would benefit from the program

The look and feel I am going for with the brochure/invitation is high-end, contemporary, carefully curated content for a very special and specific community of high-net-worth women in transition that has the resources to be and do anything they want.

Velmora
Silver Larches
Ottavin
PayRo Onyx Card
Shopping in Paris and London
Flying private
Vacationing in the Riviera & Monaco.
Beautiful people
Multi-generational - kids and grandkids.

The theme, feel, and messaging of the invitation/brochure should be consistent with the concept of moving away from – sadness, fear, regret, failure, and negative. And moving towards – joyful, happy, optimistic, exciting, successful, energetic, and contentment.

This information is intended to be informative, empowering, uplifting, transformational, and helpful - so they can lead a life that is bigger, brighter, and better than they ever dreamed of experiencing.

Target Market(s)

Wealthy woman who are currently getting divorced, recently divorced, or widowed. Generally the women will be mid-fourties and older..

Industry/Entity Type

Financial Services targeting wealthy windows and divorced woman.

Font styles to use
Serif
Sans Serif

Requirements
Must have
• The look and feel I am going for with the brochure/invitation is high-end, contemporary, carefully curated content for a very special and specific community of high-net-worth women in transition that has the resources to be and do anything they want. PLEASE ENSURE 70% OF THE WOMAN IN THE INVITATAION/BROCHURE OF NON-WHITE RACES & ETHNICITIES. The theme, feel, and messaging of the invitation/brochure should be consistent with the concept of moving away from – sadness, fear, regret, failure, and negative. And moving towards – joyful, happy, optimistic, exciting, successful, energetic, and contentment. This information is intended to be informative, empowering, uplifting, transformational, and helpful - so they can lead a life that is bigger, brighter, and better than they ever dreamed of experiencing.

```html
<!DOCTYPE html>
<html lang="en">
<head>
<meta charset="utf-8">
<title>Open Horizon Table – Invitation</title>
<link href="https://fonts.googleapis.com/css2?family=Playfair+Display:wght@400;600;700&family=Montserrat:wght@400;500;600&family=Great+Vibes&display=swap" rel="stylesheet">
<style>
  :root{
    --navy:#1f2347;
    --peach:#f1b5a0;
    --ink-light:#e6e6ef;
    --white:#ffffff;
    --dark:#1d1d2b;
    --pink-top:#f6cfcb;
    --pink-bottom:#f0b3b4;
    --rose:#e89a9d;
    --orange:#f2a25a;
    --line:#d9b3b3;
  }
  *{box-sizing:border-box;margin:0;padding:0}
  html,body{width:776px;height:1200px;overflow:hidden;background:var(--white)}
  .canvas{position:relative;width:776px;height:1200px;overflow:hidden;font-family:'Montserrat',sans-serif}

  /* ---------- Spread ---------- */
  .spread{position:absolute;left:0;top:0;width:776px;height:600px;display:flex}
  .panel-inside{width:388px;height:600px;background:var(--navy);color:var(--ink-light);padding:30px 20px 0 22px;position:relative}
  .panel-inside h2{font-family:'Playfair Display',serif;font-weight:600;color:var(--peach);font-size:17px;margin-bottom:10px}
  .panel-inside p{font-size:6.6px;line-height:1.55;margin-bottom:6px;text-align:justify}
  .two-col{display:grid;grid-template-columns:1fr 1fr;column-gap:16px}
  .section{margin-bottom:12px}
  .benefits{display:grid;grid-template-columns:1fr 1fr;column-gap:16px;row-gap:6px;list-style:none}
  .benefits li{font-size:6.8px;line-height:1.5;padding-left:9px;position:relative}
  .benefits li::before{content:"";position:absolute;left:0;top:3px;width:4px;height:4px;border-radius:50%;background:var(--peach)}
  .contact-line{position:absolute;left:22px;bottom:22px;font-size:7px;letter-spacing:1.2px;color:var(--peach)}

  .panel-cover{width:388px;height:600px;background:var(--white);position:relative}
  .cover-art{position:absolute;left:40px;top:20px;width:300px;height:340px;border-radius:6px;
    background:radial-gradient(circle at 62% 70%, rgba(242,162,90,.55) 0 22%, transparent 23%),
               radial-gradient(circle at 40% 30%, #f7e4d8 0, #fbf1ea 55%, #ffffff 80%)}
  .vertical-note{position:absolute;top:150px;font-size:6.5px;letter-spacing:2px;color:var(--navy);writing-mode:vertical-rl;font-weight:500}
  .vertical-note.left{left:12px;transform:rotate(180deg)}
  .vertical-note.right{right:12px}
  .cover-title{position:absolute;left:0;right:0;top:385px;text-align:center;color:var(--navy)}
  .cover-title .kicker{font-family:'Playfair Display',serif;font-size:22px;letter-spacing:3px;font-weight:400}
  .cover-title .script{font-family:'Great Vibes',cursive;font-size:66px;line-height:1;margin-top:-2px}
  .cover-title .label{font-size:10px;letter-spacing:4px;margin-top:14px;font-weight:500}

  /* ---------- Wellness page ---------- */
  .wellness{position:absolute;left:0;top:600px;width:776px;height:600px;
    background:linear-gradient(180deg,var(--pink-top),var(--pink-bottom));color:var(--white)}
  .floral{position:absolute;top:16px;width:90px;height:70px;border-radius:50%;
    background:radial-gradient(circle,#ffffff 0,#ecdcf0 45%,rgba(236,220,240,0) 72%)}
  .floral.left{left:120px}.floral.right{right:120px}
  .wellness h1{position:absolute;left:0;right:0;top:26px;text-align:center;font-family:'Playfair Display',serif;font-weight:400;font-size:40px;color:var(--white)}
  .portrait{position:absolute;left:260px;top:78px;width:256px;height:270px;
    background:linear-gradient(180deg,#e9c6bd 0%,#d89a8a 55%,#f1d4d0 100%);border-radius:4px}
  .dims{position:absolute;top:92px;width:235px}
  .dims.left{left:24px}.dims.right{left:528px}
  .dim{margin-bottom:12px}
  .dim h3{font-family:'Playfair Display',serif;font-weight:400;font-size:18px;margin-bottom:2px}
  .dim p{font-size:7.4px;line-height:1.5}

  .details{position:absolute;left:24px;top:420px;width:380px;height:150px;background:var(--white);border-radius:6px;padding:12px 16px}
  .details .row{display:flex;align-items:flex-end;height:32px;border-bottom:1px solid var(--line)}
  .details .row:last-child{border-bottom:none}
  .details .key{font-size:8.5px;font-weight:600;letter-spacing:1px;color:var(--dark);width:90px;padding-bottom:6px}
  .speakers{position:absolute;left:430px;top:425px;display:flex;gap:14px}
  .speaker{width:96px;height:96px;border-radius:50%;border:4px solid var(--white);
    background:linear-gradient(160deg,#d6a08f,#9a6a5d)}
  .speaker:nth-child(2){margin-top:20px;background:linear-gradient(160deg,#e0b4a5,#a77563)}
  .speaker:nth-child(3){background:linear-gradient(160deg,#c99080,#7e5548)}
</style>
</head>
<body>
<div class="canvas">

  <section class="spread">
    <div class="panel-inside">
      <div class="section">
        <h2>What, How &amp; Why I Do My Job</h2>
        <div class="two-col">
          <div>
            <p>As a wealth manager, the "what" and "how" aspects of my job are not materially different from most of my competitors. However, the thing that makes me completely unique, and without competition, is "why" I do my job.</p>
            <p>I do this because so many women experience unwelcome feelings when their marriage ends, and there is virtually no good place to obtain the important information they truly need to move forward and lead a happy, full, prosperous and fun life.</p>
          </div>
          <div>
            <p>For example, some experience shame or fear that they have failed. Others struggle with the belief they wasted a significant portion of their life. Some struggle with unresolved anger over the entire experience, and it is hard to work through alone.</p>
            <p>Usually, these negative feelings are most intense when looking backward in time. However, I have seen women go on to lead remarkably impressive lives, fuller, richer and more rewarding than they expected possible.</p>
          </div>
        </div>
      </div>
      <div class="section">
        <h2>Why I Do What I Do</h2>
        <p>I created Open Horizon Table so women in transition have a safe, supportive and comfortable space to support each other. While each woman's story is unique, the emotional consequences are fairly common and no one needs to feel alone as they process difficult, conflicting and unpredictable emotions.</p>
        <p>I want them to connect because they share a great appreciation and empathy for what the other women are experiencing. Attending each dinner forges friendships and connections, so they can be resources to each other when they need help.</p>
        <p>IMPORTANT NOTE: THIS IS NOT A THERAPY OR SUPPORT GROUP. Instead, this is a select group of very successful and accomplished women with a shared experience, who learn important information in a safe place and share their strength and hope.</p>
      </div>
      <div class="section">
        <h2>Benefits Of This Program</h2>
        <ul class="benefits">
          <li>Intimate dinner in a private room at a 5 star restaurant in Chicago</li>
          <li>This is an intimate gathering of approximately 4-10 women</li>
          <li>There is no cost to attend the event and you are welcome to attend as many as you like</li>
          <li>I will be covering the cost of dinner, drinks, valet parking and the presenter</li>
        </ul>
      </div>
      <div class="contact-line">312 555 0148 | HELLO@OPENHORIZONTABLE.COM | WWW.OPENHORIZONTABLE.COM</div>
    </div>

    <div class="panel-cover">
      <span class="vertical-note left">CONNECT WITH EACH OTHER</span>
      <div class="cover-art" role="img" aria-label="Line-art portrait illustration with a soft orange circle and dotted accents"></div>
      <span class="vertical-note right">CONNECT WITH EACH OTHER</span>
      <div class="cover-title">
        <div class="kicker">OPEN HORIZON</div>
        <div class="script">Table</div>
        <div class="label">INVITATION</div>
      </div>
    </div>
  </section>

  <section class="wellness">
    <div class="floral left" role="img" aria-label="Watercolour flower ornament"></div>
    <div class="floral right" role="img" aria-label="Watercolour flower ornament"></div>
    <h1>8 Dimensions of Wellness</h1>
    <div class="portrait" role="img" aria-label="Photo of a smiling woman in a pink blouse"></div>

    <div class="dims left">
      <div class="dim"><h3>Physical</h3><p>Physical Activity, Good Nutrition, Sleep, Preventing Illness &amp; Injury, and Managing Chronic Health Conditions.</p></div>
      <div class="dim"><h3>Emotional</h3><p>Coping effectively with life and creating satisfying relationships.</p></div>
      <div class="dim"><h3>Social</h3><p>Developing a sense of connection, belonging, and a well-developed support system.</p></div>
      <div class="dim"><h3>Intellectual</h3><p>Recognizing one's creative abilities and finding ways to expand knowledge and skills. Boost cognitive function, stimulate the brain, and fuel learning.</p></div>
    </div>
    <div class="dims right">
      <div class="dim"><h3>Spiritual</h3><p>Expanding a sense of purpose and meaning in life, including one's morals and ethics. May or may not involve religious activities. Meditation.</p></div>
      <div class="dim"><h3>Environmental</h3><p>Occupying pleasant, stimulating environments that support well-being.</p></div>
      <div class="dim"><h3>Vocational</h3><p>Gaining personal satisfaction and enrichment from one's work. Share your talents, wisdom, and experience.</p></div>
      <div class="dim"><h3>Financial</h3><p>Satisfaction with current and future financial situations.</p></div>
    </div>

    <div class="details">
      <div class="row"><span class="key">DATE/TIME</span></div>
      <div class="row"><span class="key">PRESENTER</span></div>
      <div class="row"><span class="key">PLACE</span></div>
      <div class="row"><span class="key">TOPIC</span></div>
    </div>
    <div class="speakers">
      <div class="speaker" role="img" aria-label="Portrait photo of a presenter"></div>
      <div class="speaker" role="img" aria-label="Portrait photo of a presenter"></div>
      <div class="speaker" role="img" aria-label="Portrait photo of a presenter"></div>
    </div>
  </section>

</div>
</body>
</html>
```